Business Card Design needed for start up company Pelmora

In need of a new business card designed for a start up company based in Sydney, Pelmora is a new start up innovative Company, our mission it to make property accessible for everyday Australian and to become the leading Real Estate platform in Australia. We want it to be fresh and clean.

Industry/Entity Type

Financial

Contact Information for Business Card

Section for Name
Section for Title

PELMORA - Keys Within Reach
Mobile:
Direct:

Font styles to use
Sans Serif

Colors
33a6d7
0692cd
0255a3
ffffff

Requirements
Must have
• Logo, all business card details

```html
<!DOCTYPE html>
<html lang="en">
<head>
<meta charset="utf-8">
<title>Pelmora Business Card</title>
<link href="https://fonts.googleapis.com/css2?family=Montserrat:wght@700;800&family=Open+Sans:wght@400;600&display=swap" rel="stylesheet">
<style>
  :root {
    --sky: #33a6d7;
    --ocean: #0692cd;
    --navy: #0255a3;
    --white: #ffffff;
    --paper: #f7f8f9;
    --ink-soft: #5a6b78;
    --backdrop: #e9ecef;
  }
  * { margin: 0; padding: 0; box-sizing: border-box; }
  html, body { width: 1200px; height: 1023px; overflow: hidden; }
  body {
    background: var(--backdrop);
    font-family: "Open Sans", sans-serif;
    position: relative;
  }
  .card {
    position: absolute;
    left: 220px;
    width: 760px;
    height: 434px;
    border-radius: 18px;
    overflow: hidden;
    box-shadow: 0 8px 24px rgba(0,0,0,0.14);
  }
  /* Front */
  .card-front {
    top: 48px;
    background: linear-gradient(160deg, var(--white) 0%, var(--paper) 100%);
  }
  .front-brand {
    position: absolute;
    top: 60px;
    right: 56px;
    display: flex;
    align-items: center;
    gap: 16px;
  }
  .brand-dot {
    width: 74px; height: 74px;
    border-radius: 50%;
    background: var(--sky);
  }
  .brand-name {
    font-family: "Montserrat", sans-serif;
    font-weight: 800;
    color: var(--navy);
    letter-spacing: -1px;
    line-height: 1;
  }
  .front-brand .brand-name { font-size: 72px; }
  .identity {
    position: absolute;
    left: 0;
    top: 196px;
    display: flex;
    align-items: stretch;
    gap: 14px;
  }
  .identity-mark { width: 40px; height: 62px; display: block; }
  .identity-name {
    font-family: "Montserrat", sans-serif;
    font-weight: 700;
    font-size: 30px;
    color: var(--ocean);
    line-height: 1.1;
  }
  .identity-title {
    font-size: 18px;
    color: var(--navy);
    margin-top: 2px;
  }
  .contacts {
    position: absolute;
    left: 300px;
    top: 218px;
    list-style: none;
    font-size: 16px;
    color: var(--ink-soft);
  }
  .contacts li {
    display: flex;
    align-items: center;
    gap: 12px;
    height: 30px;
  }
  .contacts svg { width: 18px; height: 18px; flex: none; }
  .front-band {
    position: absolute;
    left: 0; right: 0; bottom: 0;
    height: 66px;
    background: linear-gradient(90deg, var(--sky), var(--ocean));
    border-top: 3px solid rgba(255,255,255,0.35);
  }
  .front-band .web {
    position: absolute;
    left: 440px;
    top: 18px;
    font-size: 17px;
    color: var(--white);
    letter-spacing: 0.5px;
  }
  /* Back */
  .card-back {
    top: 540px;
    background: linear-gradient(135deg, var(--ocean) 0%, #1fb2dc 60%, #35c3e2 100%);
  }
  .back-brand {
    position: absolute;
    top: 120px;
    left: 0; right: 0;
    display: flex;
    justify-content: center;
    align-items: center;
    gap: 22px;
  }
  .back-brand .brand-dot {
    width: 120px; height: 120px;
    background: var(--white);
  }
  .back-brand .brand-name { font-size: 96px; }
  .tagline {
    position: absolute;
    top: 276px;
    left: 0; right: 0;
    display: flex;
    justify-content: center;
    align-items: center;
    gap: 14px;
    color: var(--white);
    font-size: 20px;
    letter-spacing: 0.5px;
  }
  .tagline::before, .tagline::after {
    content: "";
    width: 36px;
    height: 2px;
    background: var(--white);
  }
</style>
</head>
<body>
  <section class="card card-front" aria-label="Business card front">
    <div class="front-brand">
      <span class="brand-dot"></span>
      <span class="brand-name">PELMORA</span>
    </div>

    <div class="identity">
      <svg class="identity-mark" viewBox="0 0 40 62" aria-hidden="true">
        <polygon points="0,0 40,0 40,62 0,62" fill="var(--navy)"/>
        <polygon points="40,0 40,62 14,62" fill="var(--sky)"/>
      </svg>
      <div>
        <div class="identity-name">Your Name</div>
        <div class="identity-title">Title</div>
      </div>
    </div>

    <ul class="contacts">
      <li>
        <svg viewBox="0 0 18 18" aria-hidden="true"><circle cx="9" cy="9" r="8" fill="none" stroke="var(--ink-soft)" stroke-width="1.4"/><path d="M6 5.5c0 3.5 3 6.5 6.5 6.5l.5-1.6-1.8-.8-.8.9c-1.2-.5-2.1-1.4-2.6-2.6l.9-.8-.8-1.8z" fill="var(--ink-soft)"/></svg>
        02-555-01234
      </li>
      <li>
        <svg viewBox="0 0 18 18" aria-hidden="true"><rect x="2" y="2" width="14" height="14" rx="1.5" fill="none" stroke="var(--ink-soft)" stroke-width="1.4"/></svg>
        02-555-01234
      </li>
      <li>
        <svg viewBox="0 0 18 18" aria-hidden="true"><rect x="1" y="4" width="16" height="11" fill="var(--ocean)"/><path d="M1 4l8 6 8-6" fill="none" stroke="var(--white)" stroke-width="1.3"/></svg>
        info@pelmorahomes.com
      </li>
    </ul>

    <div class="front-band">
      <span class="web">www.pelmorahomes.com</span>
    </div>
  </section>

  <section class="card card-back" aria-label="Business card back">
    <div class="back-brand">
      <span class="brand-dot"></span>
      <span class="brand-name">PELMORA</span>
    </div>
    <p class="tagline">Keys Within Reach</p>
  </section>
</body>
</html>
```